Design of a can of the adaptogenic drink brand "Brivana" (vector)

Please take the cans from the brief and make a print-ready vector with the instructions as in the other photos.

Target Market(s)

Young, upper-middle class athlete

Industry/Entity Type

Agroalimentaire

Colors

Designer to choose colors to be used in the design.

Requirements
Must have
• Adaptogenic flawed water
Nice to have
• Sleek, classy and healthy

```html
<!DOCTYPE html>
<html lang="en">
<head>
<meta charset="utf-8">
<title>Brivana – Functional Wellness Drink Labels</title>
<link href="https://fonts.googleapis.com/css2?family=Raleway:wght@400;500;700&display=swap" rel="stylesheet">
<style>
  :root {
    --page-bg: #e3e3e5;
    --label-light: #f0f1f3;
    --wave-light: #dce8ef;
    --navy: #1a1f4d;
    --cyan: #2cc2ea;
    --ocean-top: #c8f2f4;
    --ocean-mid: #5ea9cb;
    --ocean-deep: #123f73;
    --frost: #e8eef1;
  }
  * { margin: 0; padding: 0; box-sizing: border-box; }
  html, body { width: 1200px; height: 2699px; overflow: hidden; }
  body {
    background: var(--page-bg);
    font-family: "Raleway", sans-serif;
    position: relative;
  }
  .panel {
    position: absolute;
    overflow: hidden;
    text-align: center;
  }
  .panel svg.backdrop { position: absolute; inset: 0; width: 100%; height: 100%; }
  .label { left: 96px; width: 534px; height: 597px; }
  .can { left: 763px; width: 267px; height: 657px; border-radius: 16px; }
  .panel .content { position: absolute; left: 0; right: 0; }
  .mark {
    display: block; margin: 0 auto;
    border-radius: 50%;
    border: 5px solid currentColor;
  }
  .brand { font-weight: 700; letter-spacing: 0.5px; line-height: 1; }
  .tagline { font-weight: 500; line-height: 1.3; }
  .volume { position: absolute; left: 0; right: 0; font-weight: 500; }

  .label .mark { width: 60px; height: 60px; }
  .label .content { top: 120px; }
  .label .brand { font-size: 52px; margin-top: 30px; }
  .label .tagline { font-size: 20px; margin-top: 22px; letter-spacing: 0.3px; }
  .label .volume { top: 526px; font-size: 20px; }

  .can .mark { width: 56px; height: 56px; }
  .can .content { top: 150px; }
  .can .brand { font-size: 46px; margin-top: 30px; }
  .can .tagline { font-size: 18px; margin-top: 20px; letter-spacing: 2px; }
  .can .volume { top: 556px; font-size: 19px; }

  .tone-navy { background: var(--label-light); color: var(--navy); }
  .tone-ocean { background: linear-gradient(150deg, var(--ocean-top) 0%, var(--ocean-mid) 50%, var(--ocean-deep) 100%); color: var(--frost); }
  .tone-cyan { background: var(--label-light); color: var(--cyan); }
</style>
</head>
<body>
  <svg width="0" height="0" aria-hidden="true" style="position:absolute">
    <defs>
      <linearGradient id="ocean-wave" x1="0" y1="0" x2="1" y2="1">
        <stop offset="0" stop-color="#ffffff" stop-opacity="0.12"/>
        <stop offset="1" stop-color="#ffffff" stop-opacity="0.04"/>
      </linearGradient>
    </defs>
  </svg>

  <!-- Row 1: navy edition -->
  <section class="panel label tone-navy" style="top:150px">
    <svg class="backdrop" viewBox="0 0 534 597" preserveAspectRatio="none" aria-hidden="true">
      <path d="M0 597 L0 575 C150 430 320 420 534 265 L534 597 Z" fill="var(--wave-light)"/>
    </svg>
    <div class="content">
      <span class="mark"></span>
      <h1 class="brand">Brivana</h1>
      <p class="tagline">FUNCTIONAL<br>WELLNESS DRINK</p>
    </div>
    <p class="volume">250ml</p>
  </section>
  <section class="panel can tone-navy" style="top:113px">
    <svg class="backdrop" viewBox="0 0 267 657" preserveAspectRatio="none" aria-hidden="true">
      <path d="M0 657 L0 615 C70 530 160 500 267 410 L267 657 Z" fill="var(--wave-light)"/>
    </svg>
    <div class="content">
      <span class="mark"></span>
      <h2 class="brand">Brivana</h2>
      <p class="tagline">FUNCTIONAL<br>WELLNESS DRINK</p>
    </div>
    <p class="volume">250ml</p>
  </section>

  <!-- Row 2: ocean edition -->
  <section class="panel label tone-ocean" style="top:1018px">
    <svg class="backdrop" viewBox="0 0 534 597" preserveAspectRatio="none" aria-hidden="true">
      <path d="M0 597 L0 545 C150 400 330 450 534 225 L534 597 Z" fill="url(#ocean-wave)"/>
    </svg>
    <div class="content">
      <span class="mark"></span>
      <h2 class="brand">Brivana</h2>
      <p class="tagline">FUNCTIONAL<br>WELLNESS DRINK</p>
    </div>
    <p class="volume" style="font-size:17px">250ml</p>
  </section>
  <section class="panel can tone-ocean" style="top:1012px">
    <div class="content">
      <span class="mark"></span>
      <h2 class="brand">Brivana</h2>
      <p class="tagline">FUNCTIONAL<br>WELLNESS DRINK</p>
    </div>
    <p class="volume">250ml</p>
  </section>

  <!-- Row 3: cyan edition -->
  <section class="panel label tone-cyan" style="top:1921px">
    <svg class="backdrop" viewBox="0 0 534 597" preserveAspectRatio="none" aria-hidden="true">
      <path d="M0 597 L0 575 C150 430 320 420 534 265 L534 597 Z" fill="var(--wave-light)"/>
    </svg>
    <div class="content">
      <span class="mark"></span>
      <h2 class="brand">Brivana</h2>
      <p class="tagline">FUNCTIONAL<br>WELLNESS DRINK</p>
    </div>
    <p class="volume">250ml</p>
  </section>
  <section class="panel can tone-cyan" style="top:1910px">
    <svg class="backdrop" viewBox="0 0 267 657" preserveAspectRatio="none" aria-hidden="true">
      <path d="M0 657 L0 595 C70 520 160 480 267 390 L267 657 Z" fill="#d6ecef"/>
    </svg>
    <div class="content">
      <span class="mark"></span>
      <h2 class="brand">Brivana</h2>
      <p class="tagline">FUNCTIONAL<br>WELLNESS DRINK</p>
    </div>
    <p class="volume">250ml</p>
  </section>
</body>
</html>
```